Red Fern Media Outdoor Advertising Corporate Stationery Design

We need a full corporate stationary design for our company Red Fern Media. We setup and lease billboards, building wraps, trailer ads and construction hoardings.

We need to establish our branding and our newly created logo. All our brand identity should point towards our values, vision and mission.

We are open to fresh new ideas for our stationary design as long as it ultimately reflects the brand & logo.

Corporate Stationary List:
1. Business Card Design
2. Letterhead Design
3. Email Signature Design
4. “Advertise Here” Design (for placement on empty billboards, etc)

All designs must include our logo and be kept simple, modern, friendly and effective.

All designs should please be provided in Illustrator, Photoshop and InDesign file formats.

More details are attached in Word.

Hey

The project has been guaranteed. We like what has been submitted so far but we''d like to see a few concepts for the "Advertise Here" design for open billboards please.

Thanks!

Target Market(s)

Male and female, corporates, business owners, media buying agencies, government & all age groups.

Industry/Entity Type

Construction

Requirements
Must have
• All designs must incorporate our colours: Pantone 319C, 320C, 321C & Hexachrome Black C.

1.Business Card Design
a. Logo
b. Name
c. Mobile
d. Landline
e. Website
f. Pagebook
g. Chirper
2. Letterhead Design
a. Logo
b. Mobile
c. Landline
d. Website
e. CC reg number
f. BEE level 4 contributor
g. PRAVU member
h. Postal Address
3. Email Signature Design
a. Logo
b. Name
c. Mobile
d. Landline
e. BEE level 4 contributor
f. PRAVU member
g. Website
h. Pagebook
i. Chirper
4. “Advertise Here” Design (for placement on empty billboards, etc) Majority ratio of 2:1 (eg 6m wide by 3m high) - Please use 2 attached photos.
a. Logo .co.za
b. Contact Nadia
c. Mobile
Nice to have
• Come up with a cool slogan / tagline for Business Cards, “Advertise Here” Design

```html
<!DOCTYPE html>
<html lang="en">
<head>
<meta charset="utf-8">
<title>Red Fern Media – Stationery Presentation</title>
<link rel="stylesheet" href="https://fonts.googleapis.com/css2?family=Open+Sans:wght@700&family=PT+Sans:wght@400;700&display=swap">
<style>
:root{
  --teal:#0e9fad;
  --teal-dark:#0a6f7a;
  --teal-light:#7fcdd2;
  --teal-pale:#bfe6e9;
  --ink:#111111;
  --paper:#ffffff;
  --board-top:#0b0f14;
  --board-bottom:#0d7f8a;
  --scene-bg:#d9dee2;
  --body-text:#333333;
}
*{box-sizing:border-box;margin:0;padding:0}
html,body{width:1200px;height:927px;overflow:hidden}
body{font-family:"PT Sans",sans-serif;color:var(--body-text)}
.board{position:relative;width:1200px;height:927px;overflow:hidden;
  background:linear-gradient(180deg,var(--board-top) 0%,#10161c 70%,var(--board-bottom) 100%)}

/* Billboard presentation panels */
.mount{position:absolute;background:var(--scene-bg)}
.mount--banner{left:65px;top:38px;width:455px;height:230px}
.mount--billboard{left:65px;top:309px;width:455px;height:573px}
.ad-art{position:absolute;inset:0;background:radial-gradient(ellipse at 55% 45%,#bfeff3 0%,#5fc3cc 45%,var(--teal) 100%)}
.pole-banner{position:absolute;left:182px;top:25px;width:90px;height:180px;overflow:hidden;box-shadow:0 2px 6px rgba(0,0,0,.3)}
.pole-banner .contact-box{position:absolute;left:8px;right:8px;bottom:14px;background:var(--ink);color:var(--paper);
  font-family:"Open Sans",sans-serif;font-weight:700;font-size:8px;line-height:1.3;padding:4px 5px}
.billboard{position:absolute;left:27px;top:180px;width:400px;height:200px;overflow:hidden;box-shadow:0 3px 8px rgba(0,0,0,.3)}
.billboard .contact-box{position:absolute;left:0;bottom:0;width:140px;background:var(--ink);color:var(--paper);
  font-family:"Open Sans",sans-serif;font-weight:700;font-size:15px;line-height:1.35;padding:8px 12px}

/* Letterhead */
.letterhead{position:absolute;left:574px;top:38px;width:600px;height:844px;background:var(--paper);overflow:hidden;
  box-shadow:6px 6px 0 var(--teal-dark)}
.letterhead svg{position:absolute;left:0}
.letterhead__header{top:0}
.letterhead__footer{bottom:0}
.brand{position:absolute;display:flex;align-items:center;gap:8px;font-weight:700}
.brand__mark{width:16px;height:16px;background:currentColor;display:block}
.letterhead .brand{left:27px;top:58px;color:var(--paper);font-size:24px}
.address{position:absolute;left:27px;top:105px;color:var(--paper);font-size:12.5px;line-height:1.27}
.contacts{position:absolute;right:16px;top:105px;text-align:right;color:var(--teal);font-size:12.5px;line-height:1.27}
.contacts .web{font-style:italic}
.letter{position:absolute;left:27px;top:222px;width:545px;font-size:12.5px;line-height:1.18;color:var(--body-text)}
.letter p{margin-bottom:14px}
.letter .indent{text-indent:30px}
.signature{width:110px;height:22px;margin:4px 0 2px 0;background:linear-gradient(90deg,#e6e6e6,#f6f6f6);border-radius:3px}
.signature + .signer{padding-left:14px;font-size:12px}
.legal{position:absolute;left:27px;bottom:26px;color:var(--paper);font-size:12.5px;line-height:1.3}

/* Business cards */
.card{position:absolute;width:258px;height:145px;border-radius:10px;overflow:hidden;box-shadow:3px 4px 8px rgba(0,0,0,.35)}
.card--back{left:588px;top:543px;background:var(--teal-light);color:var(--paper)}
.card--back .mini-mark{position:absolute;left:117px;top:12px;width:20px;height:16px;background:var(--ink)}
.card--back .details{position:absolute;left:76px;top:36px;font-size:10px;line-height:1.3}
.social{position:absolute;left:0;right:0;height:14px;background:var(--ink);font-size:9px;line-height:14px;color:var(--paper)}
.social--left{top:100px;right:150px;padding-left:14px}
.social--right{top:116px;left:90px;text-align:right;padding-right:14px}
.social i{position:absolute;top:2px;width:10px;height:10px;background:var(--paper)}
.social--left i{left:2px}
.social--right i{right:2px}
.social--back{top:108px;height:6px}
.card--front{left:781px;top:471px;background:var(--ink)}
.card--front .brand{left:62px;top:42px;color:var(--teal);font-size:22px}
.card--front .name-band{position:absolute;left:0;right:0;top:92px;height:28px;background:var(--teal-light);color:var(--paper);
  text-align:center;font-size:10px;line-height:1.25;padding-top:2px;padding-left:80px}
.card--front .name-band::before{content:"";position:absolute;left:0;top:0;width:90px;height:28px;background:linear-gradient(90deg,var(--teal-light),#4eb1b9)}
</style>
</head>
<body>
<main class="board">

  <section class="mount mount--banner" aria-label="Advertise here pole banner">
    <div class="pole-banner">
      <div class="ad-art" role="img" aria-label="Cartoon illustration of a figure hammering a giant stake into the banner, on a teal glow"></div>
      <div class="contact-box">Contact Nadia<br>00 00000000</div>
    </div>
  </section>

  <section class="mount mount--billboard" aria-label="Advertise here billboard">
    <div class="billboard">
      <div class="ad-art" role="img" aria-label="Cartoon illustration of a figure hammering a giant stake into the billboard, on a teal glow"></div>
      <div class="contact-box">Contact Nadia<br>00 00000000</div>
    </div>
  </section>

  <article class="letterhead" aria-label="Letterhead">
    <svg class="letterhead__header" width="600" height="215" viewBox="0 0 600 215" aria-hidden="true">
      <rect width="600" height="215" fill="var(--teal)"/>
      <path d="M120 215 C320 210 420 60 600 22 L600 215 Z" fill="var(--teal-light)"/>
      <path d="M175 215 C350 212 450 70 600 36 L600 215 Z" fill="var(--paper)"/>
    </svg>
    <div class="brand"><span class="brand__mark"></span>Red Fern Media</div>
    <div class="address">Business address<br>line 2<br>City Name<br>Post code<br>Country</div>
    <div class="contacts">Mobile-00 000000000<br>Landline-000 0000000<br><span class="web">http://redfernmedia.com</span></div>

    <div class="letter">
      <p>Dear ________</p>
      <p class="indent">Dummy letter text here. Dummy letter text here. Dummy letter text here. Dummy letter text here. Dummy letter text here. Dummy letter text here. Dummy letter text here. Dummy letter text here. Dummy letter text here.</p>
      <p>Dummy letter text here. Dummy letter text here. Dummy letter text here. Dummy letter text here. Dummy letter text here. Dummy letter text here. Dummy letter text here. Dummy letter text here. Dummy letter text here. Dummy letter text here. Dummy letter text here. Dummy letter text here. Dummy letter text here. Dummy letter text here. Dummy letter text here.</p>
      <p>Dummy letter text here. Dummy letter text here. Dummy letter text here. Dummy letter text here.</p>
      <p>Kind regards</p>
      <div class="signature" role="img" aria-label="Handwritten signature"></div>
      <div class="signer">[John Smith]</div>
    </div>

    <svg class="letterhead__footer" width="600" height="110" viewBox="0 0 600 110" aria-hidden="true">
      <path d="M0 22 C200 -8 420 70 600 40 L600 110 L0 110 Z" fill="var(--teal-light)"/>
      <path d="M0 30 C200 2 420 78 600 50 L600 110 L0 110 Z" fill="var(--teal)"/>
    </svg>
    <div class="legal">CC reg number -123456<br>BEE level 4 contributor<br>PRAVU member</div>
  </article>

  <div class="card card--back" aria-label="Business card back">
    <span class="mini-mark"></span>
    <div class="details">Mobile - 000000000<br>Landline - 000000000<br>http://redfernmedia.com</div>
    <div class="social social--back"></div>
    <div class="social social--left"><i></i>find us on pagebook</div>
    <div class="social social--right"><i></i>follow us on chirper</div>
  </div>

  <div class="card card--front" aria-label="Business card front">
    <div class="brand"><span class="brand__mark"></span>Red Fern Media</div>
    <div class="name-band">John Smith<br>DESIGNATION</div>
  </div>

</main>
</body>
</html>
```